home theater/ flat panel TV installation/ computer networking

single page flyer front and back, I am paying for adress labels so it should be 8 1/2" x 11" tri-fold with a place for the labels to go and be easy to mail.

Brightline Media

Charlotte NC 28391

http://www.brightlinemedianc.example/

call today for your no cost consultation  704-582-3946

Call today for your no cost consultation!    704-582-3946  Brightline Media

If your new home came with a finished basement, or you are

finishing it yourself, consider making part of it into a great home

theater. Why not add a fantastic High Definition projector and 100”

screen to your lovely new home? Experience satellite and cable TV,

video games, and of course, movies like you have never seen or

heard before. The cost of the system is probably a lot less than you

think. Finally, we install everything and provide a single programmed

remote to operate the entire system, easily! Already have a High

Definition TV? Let us integrate it with speakers, programmable

remotes, even a popcorn machine! Free consultations at your

request.

professional home theater designer and network cable installations in Texas

regular size.  I am picturing 8 1/2" x 11"  tri-fold.   I have never had a flyer before and am willing to accept different sizes.   

 

Target Market(s)

These will be sent to new home owners already looking for these services. I am a small company trying to say "we are the best".

These are the services we sell... (feel free to High-light or bullet)

-Home Theater
-High Definition TV
-Surround Sound
-All-in-One remotes
-Computer Networks
-Liscenced Electrician
-Lighting control

Industry/Entity Type

Computer

Requirements
Must have
• most of these photos. I am willing to pay for something better if available.  maybe a family or something.

• customer testimonial (should be italisized)

• "Brightline Media showed up on time, cleaned up after themselves, they we great!"

• "...we left the key under the mat, when we got home the TV was on the wall..."
Nice to have
• sonic wave from business card.eps file
• a few more photos

```html
<!DOCTYPE html>
<html lang="en">
<head>
<meta charset="utf-8">
<title>Brightline Media Mailer</title>
<link rel="stylesheet" href="https://fonts.googleapis.com/css2?family=Arimo:ital,wght@0,400;0,700;1,400&display=swap">
<style>
  :root {
    --ink: #1f1f1f;
    --muted: #555;
    --blue: #2b93d6;
    --orange: #f08a24;
    --paper: #ffffff;
    --frame: #222;
    --label-line: #9a9a9a;
    --wall-top: #f7f7f7;
    --wall-bottom: #e4e4e4;
    --wood-top: #d9a86a;
    --wood-bottom: #b98245;
  }
  * { box-sizing: border-box; margin: 0; padding: 0; }
  html, body {
    width: 1200px; height: 776px; overflow: hidden;
    background: var(--paper);
    font-family: "Arimo", Arial, sans-serif;
    color: var(--ink);
  }
  .canvas { position: relative; width: 1200px; height: 776px; }

  /* Mailing side */
  .mailer-back {
    position: absolute; left: 44px; top: 270px; width: 786px; height: 486px;
    background: var(--paper); border: 2px solid var(--frame);
  }
  .back-name {
    position: absolute; left: 16px; top: 44px;
    font-size: 37px; font-weight: 400; letter-spacing: 1px; color: var(--ink);
  }
  .back-tagline {
    position: absolute; left: 70px; top: 86px;
    font-size: 13px; color: var(--ink); letter-spacing: 0.3px;
  }
  .qualities {
    position: absolute; left: 16px; top: 164px;
    font-size: 13px; font-weight: 700; letter-spacing: 0.2px;
  }
  .services {
    position: absolute; left: 16px; top: 207px; list-style: none;
    font-size: 12px; line-height: 21.3px;
  }
  .services li::before { content: "- "; }
  .mailing-label {
    position: absolute; left: 346px; top: 226px; width: 240px; height: 148px;
    border: 1.5px dashed var(--label-line);
    display: flex; align-items: center; justify-content: center;
    font-size: 13px; color: var(--label-line); letter-spacing: 0.5px;
  }
  .testimonials { position: absolute; left: 16px; top: 354px; width: 300px; }
  .testimonials h2 { font-size: 12px; font-weight: 700; margin-bottom: 6px; }
  .testimonial { margin-bottom: 10px; }
  .testimonial q { display: block; font-size: 10.5px; font-style: italic; line-height: 12px; quotes: "\201C" "\201D"; }
  .testimonial cite { display: block; font-size: 9.5px; font-style: normal; color: var(--muted); margin-top: 2px; }
  .testimonial cite b { color: var(--ink); }
  .return-address {
    position: absolute; left: 516px; top: 380px; font-style: normal;
    font-size: 13px; line-height: 17px;
  }
  .return-address strong { display: block; font-size: 15px; }
  .back-web {
    position: absolute; left: 0; right: 0; top: 455px; text-align: center;
    font-size: 12px; font-weight: 700;
  }

  /* Front panel */
  .mailer-front {
    position: absolute; left: 558px; top: 28px; width: 634px; height: 436px;
    background: var(--paper); border: 2px solid var(--frame); overflow: hidden;
  }
  .scene-wall {
    position: absolute; left: 0; top: 0; width: 100%; height: 160px;
    background: linear-gradient(180deg, var(--wall-top), var(--wall-bottom));
  }
  .scene-floor {
    position: absolute; left: 0; bottom: 0; width: 100%; height: 72px;
    background: linear-gradient(180deg, var(--wood-top), var(--wood-bottom));
  }
  .front-name {
    position: absolute; right: 28px; top: 150px;
    font-size: 46px; font-weight: 400; color: var(--blue); letter-spacing: 0.5px;
  }
  .front-tagline {
    position: absolute; right: 30px; top: 214px;
    font-size: 18px; color: var(--blue);
  }
  .front-tagline .dot { color: var(--orange); }
  .front-copy {
    position: absolute; left: 22px; top: 250px; width: 594px;
    font-size: 10.5px; line-height: 14px; color: #333;
  }
  .front-copy p + p { margin-top: 14px; }
  .front-cta {
    position: absolute; left: 22px; top: 370px;
    font-size: 11px; font-weight: 700; color: #2a2a2a;
  }
  .front-cta span { font-weight: 400; margin-left: 10px; }
  .front-web {
    position: absolute; left: 0; right: 0; top: 390px; text-align: center;
    font-size: 11px; font-weight: 700; color: #2a2a2a;
  }
</style>
</head>
<body>
<main class="canvas">

  <section class="mailer-back">
    <div class="back-name">BRIGHTLINE MEDIA</div>
    <div class="back-tagline">Audio • Video • Structured Wiring</div>

    <div class="qualities">EXPERIENCED • PROFESSIONAL • RELIABLE</div>
    <ul class="services">
      <li>Home Theater</li>
      <li>High Definition TV</li>
      <li>Surround Sound</li>
      <li>All-in-One remotes</li>
      <li>Computer Networks</li>
      <li>Licensed Electrician</li>
      <li>Lighting control</li>
    </ul>

    <div class="mailing-label">MAILING LABEL</div>

    <div class="testimonials">
      <h2>customer testimonials</h2>
      <div class="testimonial">
        <q>Brightline Media showed up on time, cleaned up after themselves, they were great!</q>
        <cite><b>Dale,</b> Charlotte</cite>
      </div>
      <div class="testimonial">
        <q>...we left the key under the mat, when we got home the TV was on the wall...</q>
        <cite><b>Mark T.,</b> Charlotte</cite>
      </div>
    </div>

    <address class="return-address">
      <strong>Brightline Media</strong>
      704-582-3946<br>
      Charlotte NC 28391
    </address>

    <div class="back-web">www.brightlinemedianc.example</div>
  </section>

  <section class="mailer-front">
    <div class="scene-wall" role="img" aria-label="Flat panel TV and wall speaker mounted on a white wall"></div>
    <div class="scene-floor" role="img" aria-label="Wooden floor"></div>

    <div class="front-name">BRIGHTLINE MEDIA</div>
    <div class="front-tagline">Audio <span class="dot">•</span> Video <span class="dot">•</span> Structured Wiring</div>

    <div class="front-copy">
      <p>If your new home came with a finished basement, or you are finishing it yourself, consider making part of it into a great home theater. Why not add a fantastic High Definition projector and 100” screen to your lovely new home? Experience satellite and cable TV, video games, and of course, movies like you have never seen or heard before. The cost of the system is probably a lot less than you think.</p>
      <p>Finally, we install everything and provide a single programmed remote to operate the entire system, easily! Already have a High Definition TV? Let us integrate it with speakers, programmable remotes, even a popcorn machine!</p>
    </div>

    <div class="front-cta">Call today for your no cost consultation! <span>704-582-3946</span></div>
    <div class="front-web">www.brightlinemedianc.example</div>
  </section>

</main>
</body>
</html>
```